QT&K PPT

Take my ugly PowerPoint and make it look slick. Use our company color scheme throughout, embed our logo on a couple slides, pick out a couple of stock photos of smiling people and insert where appropriate, and provide multiple slide templates that we can work from. We are launching a new service that is all about reducing time-to-market for medical device manufacturers so include themes relating to medical device, speed, acceleration, overcoming obstacles, and/or breaking down barriers.

```html
<!DOCTYPE html>
<html lang="en">
<head>
<meta charset="utf-8">
<title>Northwind Medical – Pre-Validated Packaging Slide Templates</title>
<link href="https://fonts.googleapis.com/css2?family=Roboto:wght@300;400;500;700&display=swap" rel="stylesheet">
<style>
:root{
  --canvas:#dcdbdc;
  --navy:#1f2b3e;
  --blue:#1a7db5;
  --pale:#c5dde9;
  --ink:#23324a;
  --gray:#5f6670;
  --line:#d7dbe0;
  --chip:#eef0f2;
  --white:#ffffff;
}
*{box-sizing:border-box;margin:0;padding:0}
html,body{width:1200px;height:2446px;overflow:hidden}
body{background:var(--canvas);font-family:"Roboto",Arial,sans-serif;color:var(--ink);position:relative}
.slide{position:absolute;width:54em;height:30.3em;overflow:hidden;background:var(--white);font-size:10px}
.slide.hero{left:160px;top:84px;font-size:16.3px}
.deco{position:absolute;left:0;top:0;width:54em;height:28.5em}
.deco circle{fill:var(--pale)}
.blue-deco .deco circle{fill:var(--blue)}
.photo-deco .deco circle{fill:rgba(255,255,255,.22)}
.white-deco .deco circle{fill:var(--white)}
.photo-bg{position:absolute;left:0;top:0;width:54em;height:28.5em;background:linear-gradient(120deg,#243349 0%,#2c3d56 45%,#3a4b63 70%,#25344a 100%)}
.dark{background:var(--navy)}
.band{position:absolute;left:0;bottom:0;width:54em;height:1.8em;background:var(--navy);display:flex;align-items:center;justify-content:center}
.dark .band{background:var(--blue)}
.band span{font-size:.55em;color:var(--white);font-weight:500}

/* brand lockup: plain circle + name */
.brand{position:absolute;display:flex;align-items:center}
.brand .dot{width:2.6em;height:2.6em;border-radius:50%;background:var(--blue);margin-right:.6em;flex:none}
.brand .name{font-size:2.5em;font-weight:400;line-height:1;color:var(--navy);white-space:nowrap}
.dark .brand .name{color:var(--white)}

.title-block{position:absolute;left:4.8em;top:12.2em}
.title-block h1{font-size:2.75em;line-height:1.1;font-weight:700;color:var(--navy)}
.dark .title-block h1{color:var(--white)}
.rule{position:absolute;height:.3em;background:var(--blue);border-radius:.2em}
.dark .rule{background:var(--white)}
.subtitle{position:absolute;left:4.8em;top:19.8em;white-space:nowrap}
.subtitle span{font-size:1.05em;color:var(--gray)}
.dateline{position:absolute;left:4.8em;top:23.5em}
.dateline span{font-size:.66em;color:var(--gray);letter-spacing:.08em;font-weight:500}
.dark .subtitle span,.dark .dateline span{color:var(--white)}

/* content footer */
.foot{position:absolute;left:1.4em;right:1.4em;bottom:1em;height:1.8em;display:flex;align-items:center}
.foot .brand{position:static}
.foot .brand .dot{width:1.2em;height:1.2em;margin-right:.3em}
.foot .brand .name{font-size:1.15em}
.foot .pill{flex:1;height:1.4em;margin-left:1em;background:#f2f3f5;border-radius:.7em;display:flex;align-items:center;justify-content:flex-end;padding-right:1em}
.foot .pill span{font-size:.5em;color:var(--gray)}

/* requirements slide */
.lab-top{position:absolute;left:0;top:0;width:54em;height:17em;background:linear-gradient(160deg,#3d6b97 0%,#2a5683 50%,#1f4a78 100%)}
.center-head{position:absolute;left:0;width:54em;text-align:center}
.center-head h2{font-size:1.75em;font-weight:300;line-height:1.15;color:var(--white)}
.center-head p{font-size:1.2em;color:var(--white);font-weight:300}
.card{position:absolute;top:12.2em;width:15.8em;height:14.2em;background:var(--white);border-radius:1.4em 1.4em .6em .6em;box-shadow:0 .1em .6em rgba(0,0,0,.1);padding:3.1em .9em 0}
.card .ico{position:absolute;left:5.8em;top:-2.3em;width:4.2em;height:4.2em;border-radius:50%;background:var(--blue);border:.35em solid var(--white);display:flex;align-items:center;justify-content:center}
.card h3{font-size:1.02em;font-weight:400;color:var(--blue);text-align:center;line-height:1.15;padding-bottom:.4em;border-bottom:1px solid var(--line);margin-bottom:.5em}
.card ul{list-style:none}
.card li{font-size:.6em;color:var(--gray);line-height:1.3;padding-left:.9em;position:relative}
.card li::before{content:"";position:absolute;left:0;top:.5em;width:.35em;height:.35em;border-radius:50%;background:var(--blue)}

/* market slide */
.left-head{position:absolute;left:2.9em;top:2.6em}
.left-head h2{font-size:1.75em;font-weight:300;line-height:1.15;color:var(--navy)}
.left-head h2 strong{font-weight:700}
.left-head .blue{font-size:1.3em;color:var(--blue);font-weight:300;margin-top:.1em}
.bullets{position:absolute;list-style:none}
.bullets li{font-size:1.08em;color:var(--gray);line-height:1.25;margin-bottom:.35em;padding-left:1.3em;position:relative}
.bullets li::before{content:"";position:absolute;left:0;top:.35em;width:.6em;height:.6em;border-radius:50%;background:var(--blue)}
.photo-tape{position:absolute;left:28.2em;top:0;width:23em;height:24.6em;background:linear-gradient(150deg,#b9c24a 0%,#8c8f4d 35%,#b48d5f 65%,#c9a06d 100%)}
.photo-lab{position:absolute;left:3em;top:0;width:12em;height:24.6em;background:linear-gradient(170deg,#6f7781 0%,#aeb4bb 45%,#d9dde2 75%,#b8c6d6 100%)}

/* partial slide */
.cols{position:absolute;top:12.6em;display:flex}
.col{width:17.4em;padding-right:.6em}
.col + .col{border-left:1px solid var(--line);padding-left:.6em}
.col .lead{font-size:.92em;color:var(--blue);line-height:1.2;padding-left:1.2em;position:relative;margin-bottom:.2em}
.col .lead::before{content:"";position:absolute;left:0;top:.3em;width:.65em;height:.65em;border-radius:50%;background:var(--blue)}
.col ul{list-style:none;margin:0 0 .4em 2.1em}
.col li{font-size:.86em;color:var(--gray);line-height:1.35;padding-left:1em;position:relative}
.col li::before{content:"";position:absolute;left:0;top:.55em;width:.35em;height:.35em;background:var(--navy)}

/* timeline slide */
.dash{position:absolute;left:0;top:10.45em;width:54em;border-top:1px dashed #c8ccd2}
.step-ico{position:absolute;top:9em;width:3em;height:3em;border-radius:50%;background:var(--blue);display:flex;align-items:center;justify-content:center}
.step-label{position:absolute;top:12.8em;width:12em;text-align:center}
.step-label span{font-size:.98em;color:var(--blue)}
.chev{position:absolute;top:14.2em;width:11.6em;height:3.9em;background:var(--chip);clip-path:polygon(0 0,90% 0,100% 50%,90% 100%,0 100%,8% 50%);padding:.6em 0 0 1.4em}
.chev.first{clip-path:polygon(0 0,90% 0,100% 50%,90% 100%,0 100%)}
.chev ul{list-style:none}
.chev li{font-size:.55em;color:var(--gray);line-height:1.4;padding-left:.9em;position:relative}
.chev li::before{content:"";position:absolute;left:0;top:.55em;width:.3em;height:.3em;border-radius:50%;background:var(--blue)}
.down{position:absolute;top:18.7em;width:1.2em;height:1.3em}
.pv-bar{position:absolute;left:3.3em;top:20.1em;width:23.7em;height:2.2em;background:var(--blue);clip-path:polygon(0 0,96% 0,100% 50%,96% 100%,0 100%);display:flex;align-items:center}
.pv-bar span{color:var(--white);font-size:.92em;width:13em;padding-left:1em}
.note{position:absolute;left:3.7em;top:22.9em;width:22em}
.note span{font-size:.68em;color:var(--gray);line-height:1.2;display:block}

/* contact */
.contact-brand .dot{width:2em;height:2em}
.contact-brand .name{font-size:1.9em}
.contact-head{position:absolute;left:4.8em;top:17.2em}
.contact-head span{font-size:1.1em;font-weight:700;color:var(--white)}
.contact-list{position:absolute;left:4.8em;top:20.1em;list-style:none}
.contact-list li{display:flex;align-items:center;height:1.6em}
.contact-list svg{width:1em;height:1em;margin-right:.9em}
.contact-list span{font-size:.78em;color:var(--white)}
</style>
</head>
<body>

<section class="slide hero">
  <svg class="deco" viewBox="0 0 540 285" aria-hidden="true"><circle cx="470" cy="150" r="128"/></svg>
  <div class="brand" style="left:4.8em;top:5.2em"><span class="dot"></span><span class="name">Northwind Medical</span></div>
  <div class="title-block"><h1>Pre-Validated<br>Packaging</h1></div>
  <div class="rule" style="left:4.8em;top:19em;width:9em"></div>
  <div class="subtitle"><span>One and Done | MYTH vs Reality | Packaging Validation</span></div>
  <div class="dateline"><span>Wednesday, February 1, 2023</span></div>
  <div class="band"><span>© 2023 Northwind Medical, Inc.</span></div>
</section>

<section class="slide" style="left:51px;top:806px">
  <svg class="deco" viewBox="0 0 540 285" aria-hidden="true"><circle cx="470" cy="150" r="128"/></svg>
  <div class="brand" style="left:4.8em;top:5.2em"><span class="dot"></span><span class="name">Northwind Medical</span></div>
  <div class="title-block"><h1>Pre-Validated<br>Packaging</h1></div>
  <div class="rule" style="left:4.8em;top:19em;width:9em"></div>
  <div class="subtitle"><span>One and Done | MYTH vs Reality | Packaging Validation</span></div>
  <div class="dateline"><span>Wednesday, February 1, 2023</span></div>
  <div class="band"><span>© 2023 Northwind Medical, Inc.</span></div>
</section>

<section class="slide blue-deco" style="left:608px;top:806px">
  <svg class="deco" viewBox="0 0 540 285" aria-hidden="true"><circle cx="470" cy="150" r="128"/></svg>
  <div class="brand" style="left:4.8em;top:5.2em"><span class="dot"></span><span class="name">Northwind Medical</span></div>
  <div class="title-block"><h1>Pre-Validated<br>Packaging</h1></div>
  <div class="rule" style="left:4.8em;top:19em;width:9em"></div>
  <div class="subtitle"><span>One and Done | MYTH vs Reality | Packaging Validation</span></div>
  <div class="dateline"><span>Wednesday, February 1, 2023</span></div>
  <div class="band"><span>© 2023 Northwind Medical, Inc.</span></div>
</section>

<section class="slide dark photo-deco" style="left:51px;top:1127px">
  <div class="photo-bg" role="img" aria-label="Dimmed photo of a packaging lab with sealing equipment"></div>
  <svg class="deco" viewBox="0 0 540 285" aria-hidden="true"><circle cx="470" cy="150" r="128"/></svg>
  <div class="brand" style="left:4.8em;top:5.2em"><span class="dot"></span><span class="name">Northwind Medical</span></div>
  <div class="title-block"><h1>Pre-Validated<br>Packaging</h1></div>
  <div class="rule" style="left:4.8em;top:19em;width:9em"></div>
  <div class="subtitle"><span>One and Done | MYTH vs Reality | Packaging Validation</span></div>
  <div class="dateline"><span>Wednesday, February 1, 2023</span></div>
  <div class="band"><span>© 2023 Northwind Medical, Inc.</span></div>
</section>

<section class="slide dark white-deco" style="left:608px;top:1127px">
  <div class="photo-bg" role="img" aria-label="Dimmed photo of a packaging lab with sealing equipment"></div>
  <svg class="deco" viewBox="0 0 540 285" aria-hidden="true"><circle cx="470" cy="150" r="128"/></svg>
  <div class="brand" style="left:4.8em;top:5.2em"><span class="dot"></span><span class="name">Northwind Medical</span></div>
  <div class="title-block"><h1>Pre-Validated<br>Packaging</h1></div>
  <div class="rule" style="left:4.8em;top:19em;width:9em"></div>
  <div class="subtitle"><span>One and Done | MYTH vs Reality | Packaging Validation</span></div>
  <div class="dateline"><span>Wednesday, February 1, 2023</span></div>
  <div class="band"><span>© 2023 Northwind Medical, Inc.</span></div>
</section>

<section class="slide" style="left:51px;top:1449px">
  <div class="lab-top" role="img" aria-label="Blue-tinted photo of a medical packaging lab"></div>
  <div class="center-head" style="top:2.8em"><h2>What is required of a fully Validated Sterile Barrier<br>Packaging System?</h2></div>
  <div class="center-head" style="top:8.1em"><p>Which of these benchmarks can be Pre-Validated?</p></div>
  <div class="card" style="left:2.5em">
    <div class="ico"><svg width="18" height="18" viewBox="0 0 24 24" fill="none" stroke="#fff" stroke-width="1.6"><path d="M3 8l9-4 9 4v9l-9 4-9-4z"/><path d="M3 8l9 4 9-4M12 12v9"/></svg></div>
    <h3>Package<br>Design</h3>
    <ul><li>Microbial Barrier properties</li><li>Sterilization compatibility</li><li>Box: shelf and shipping carton (protective packaging)</li><li>Biocompatibility/toxicity attributes</li><li>Compatibility of device and package materials</li><li>Compatibility with labeling</li></ul>
  </div>
  <div class="card" style="left:19.1em">
    <div class="ico"><svg width="18" height="18" viewBox="0 0 24 24" fill="none" stroke="#fff" stroke-width="1.6"><circle cx="12" cy="12" r="3.5"/><circle cx="12" cy="12" r="8" stroke-dasharray="3 2"/></svg></div>
    <h3>Process<br>Validation</h3>
    <ul><li>Develop Sealing Parameters</li><li>Sealer IQ, OQ and PQ</li></ul>
  </div>
  <div class="card" style="left:35.7em">
    <div class="ico"><svg width="18" height="18" viewBox="0 0 24 24" fill="none" stroke="#fff" stroke-width="1.6"><rect x="4" y="4" width="16" height="16" rx="2"/><path d="M8 15v-3M12 15V9M16 15v-5"/></svg></div>
    <h3>Package Performance<br>Transit Testing</h3>
    <ul><li>Environmental Conditioning</li><li>Distribution Simulation</li><li>Aging (accelerated &amp; real time)</li><li>Aseptic presentation</li></ul>
  </div>
  <div class="foot"><div class="brand"><span class="dot"></span><span class="name">Northwind Medical</span></div><div class="pill"><span>© 2023 Northwind Medical, Inc. &nbsp;| &nbsp;5</span></div></div>
</section>

<section class="slide" style="left:608px;top:1449px">
  <div class="left-head"><h2>What’s available currently on<br>the <strong>“Pre-Validated”</strong> market?</h2></div>
  <div class="rule" style="left:2.9em;top:7.1em;width:6.2em;height:.25em"></div>
  <ul class="bullets" style="left:2.9em;top:10.7em;width:24em">
    <li>Generic sterile barrier systems</li>
    <li>Accelerated aging</li>
    <li>Compatible with various sterilization modalities.</li>
    <li>Sealer Validations</li>
    <li>Packaging Materials in stock</li>
  </ul>
  <div class="photo-tape" role="img" aria-label="Photo of a worker in a safety vest sealing a cardboard box with a tape gun"></div>
  <div class="foot"><div class="brand"><span class="dot"></span><span class="name">Northwind Medical</span></div><div class="pill"><span>© 2023 Northwind Medical, Inc. &nbsp;| &nbsp;6</span></div></div>
</section>

<section class="slide" style="left:51px;top:1771px">
  <div class="photo-lab" role="img" aria-label="Photo of a lab technician handling sample vials at a testing station"></div>
  <div class="left-head" style="left:16.9em;top:1.9em"><h2>Pre-Validated really means<br><strong>“Partially Validated”.</strong></h2><p class="blue">What is still required?</p></div>
  <div class="cols" style="left:16.9em">
    <div class="col">
      <p class="lead">Distribution testing</p>
      <ul><li>Environmental conditioning</li><li>Distribution simulation</li><li>Sterile barrier testing</li></ul>
      <p class="lead">Sterilization validation</p>
      <p class="lead">Device-specific requirements:</p>
      <ul><li>Accelerated aging</li><li>Real-time aging</li><li>Label design</li></ul>
    </div>
    <div class="col">
      <p class="lead">Missing critical components of a ‘World-Class’ packaging system:</p>
      <ul><li>Label abrasion test</li><li>Human factors testing</li><li>Documentation of process risk assessment</li><li>Preconfigured shipping carton</li><li>Submission-ready data set</li></ul>
    </div>
  </div>
  <div class="foot"><div class="brand"><span class="dot"></span><span class="name">Northwind Medical</span></div><div class="pill"><span>© 2023 Northwind Medical, Inc. &nbsp;| &nbsp;7</span></div></div>
</section>

<section class="slide" style="left:608px;top:1771px">
  <div class="center-head" style="top:2.4em"><h2 style="color:var(--navy)">How is The Timeline Affected?</h2></div>
  <div class="rule" style="left:22.4em;top:5.3em;width:9.2em;height:.25em"></div>
  <div class="center-head" style="top:7em"><p style="color:var(--blue);font-size:1.08em;font-weight:400">Traditional Packaging Validations take 26 – 30 weeks to complete</p></div>
  <div class="dash"></div>
  <div class="step-ico" style="left:7.3em"><svg width="16" height="16" viewBox="0 0 24 24" fill="none" stroke="#fff" stroke-width="1.8"><path d="M3 8l9-4 9 4v9l-9 4-9-4z"/><path d="M3 8l9 4 9-4M12 12v9"/></svg></div>
  <div class="step-ico" style="left:19.5em"><svg width="16" height="16" viewBox="0 0 24 24" fill="none" stroke="#fff" stroke-width="1.8"><circle cx="12" cy="12" r="3.5"/><circle cx="12" cy="12" r="8" stroke-dasharray="3 2"/></svg></div>
  <div class="step-ico" style="left:31.7em"><svg width="16" height="16" viewBox="0 0 24 24" fill="none" stroke="#fff" stroke-width="1.8"><circle cx="7" cy="8" r="3"/><circle cx="17" cy="8" r="3"/><path d="M4 20h16M12 12v8"/></svg></div>
  <div class="step-ico" style="left:44em"><svg width="16" height="16" viewBox="0 0 24 24" fill="none" stroke="#fff" stroke-width="1.8"><rect x="3" y="9" width="12" height="8"/><path d="M15 12h4l2 3v2h-6"/><circle cx="7" cy="18" r="1.5"/><circle cx="17" cy="18" r="1.5"/></svg></div>
  <div class="step-label" style="left:2.8em"><span>Package Design</span></div>
  <div class="step-label" style="left:15em"><span>Process Validation</span></div>
  <div class="step-label" style="left:27.2em"><span>Stability Studies</span></div>
  <div class="step-label" style="left:39.5em"><span>Distribution Studies</span></div>
  <div class="chev first" style="left:3.2em"><ul><li>Sterile barrier</li><li>Packaging System</li><li>Labeling</li></ul></div>
  <div class="chev" style="left:15.4em"><ul><li>Sealer settings</li><li>OQ, PQ</li></ul></div>
  <div class="chev" style="left:27.6em"><ul><li>Real time aging</li></ul></div>
  <div class="chev" style="left:39.8em"><ul><li>Environmental conditioning</li><li>Transit simulation</li></ul></div>
  <svg class="down" style="left:8.2em" viewBox="0 0 12 13"><path d="M3 0h6v6h3L6 13 0 6h3z" fill="#1a7db5"/></svg>
  <svg class="down" style="left:20.4em" viewBox="0 0 12 13"><path d="M3 0h6v6h3L6 13 0 6h3z" fill="#1a7db5"/></svg>
  <div class="pv-bar"><span>✓ &nbsp;Pre-Validated</span><span>✓ &nbsp;Pre-Validated</span></div>
  <div class="note"><span>Currently available Pre-Validated packaging eliminates<br>10 to 12 of those weeks</span></div>
  <div class="foot"><div class="brand"><span class="dot"></span><span class="name">Northwind Medical</span></div><div class="pill"><span>© 2023 Northwind Medical, Inc. &nbsp;| &nbsp;8</span></div></div>
</section>

<section class="slide dark photo-deco" style="left:51px;top:2093px">
  <div class="photo-bg" role="img" aria-label="Dimmed photo of a packaging lab with sealing equipment"></div>
  <svg class="deco" viewBox="0 0 540 285" aria-hidden="true"><circle cx="470" cy="150" r="128"/></svg>
  <div class="brand contact-brand" style="left:4.8em;top:12.6em"><span class="dot"></span><span class="name">Northwind Medical</span></div>
  <div class="contact-head"><span>Contact Us</span></div>
  <ul class="contact-list">
    <li><svg viewBox="0 0 24 24" fill="#fff"><path d="M6.6 10.8a15 15 0 006.6 6.6l2.2-2.2a1 1 0 011-.25 11 11 0 003.6.6 1 1 0 011 1V20a1 1 0 01-1 1A17 17 0 013 4a1 1 0 011-1h3.5a1 1 0 011 1 11 11 0 00.6 3.6 1 1 0 01-.25 1z"/></svg><span>(555) 014-2290</span></li>
    <li><svg viewBox="0 0 24 24" fill="none" stroke="#fff" stroke-width="2"><circle cx="12" cy="12" r="4"/><path d="M16 12v1.5a2.5 2.5 0 005 0V12a9 9 0 10-3.5 7.1"/></svg><span>info@northwindmed.example</span></li>
    <li><svg viewBox="0 0 24 24" fill="none" stroke="#fff" stroke-width="1.8"><circle cx="12" cy="12" r="9"/><path d="M3 12h18M12 3c3 3 3 15 0 18M12 3c-3 3-3 15 0 18"/></svg><span>https://northwindmed.example</span></li>
  </ul>
  <div class="band"><span>© 2023 Northwind Medical, Inc.</span></div>
</section>

<section class="slide dark white-deco" style="left:608px;top:2093px">
  <div class="photo-bg" role="img" aria-label="Dimmed photo of a packaging lab with sealing equipment"></div>
  <svg class="deco" viewBox="0 0 540 285" aria-hidden="true"><circle cx="470" cy="150" r="128"/></svg>
  <div class="brand contact-brand" style="left:4.8em;top:12.6em"><span class="dot"></span><span class="name">Northwind Medical</span></div>
  <div class="contact-head"><span>Contact Us</span></div>
  <ul class="contact-list">
    <li><svg viewBox="0 0 24 24" fill="#fff"><path d="M6.6 10.8a15 15 0 006.6 6.6l2.2-2.2a1 1 0 011-.25 11 11 0 003.6.6 1 1 0 011 1V20a1 1 0 01-1 1A17 17 0 013 4a1 1 0 011-1h3.5a1 1 0 011 1 11 11 0 00.6 3.6 1 1 0 01-.25 1z"/></svg><span>(555) 014-2290</span></li>
    <li><svg viewBox="0 0 24 24" fill="none" stroke="#fff" stroke-width="2"><circle cx="12" cy="12" r="4"/><path d="M16 12v1.5a2.5 2.5 0 005 0V12a9 9 0 10-3.5 7.1"/></svg><span>info@northwindmed.example</span></li>
    <li><svg viewBox="0 0 24 24" fill="none" stroke="#fff" stroke-width="1.8"><circle cx="12" cy="12" r="9"/><path d="M3 12h18M12 3c3 3 3 15 0 18M12 3c-3 3-3 15 0 18"/></svg><span>https://northwindmed.example</span></li>
  </ul>
  <div class="band"><span>© 2023 Northwind Medical, Inc.</span></div>
</section>

</body>
</html>
```